Tradeshow Booth Design

Clean background, some variance of kelly green in the colors - see image for text - maybe an image with people or nice modern homes...

Target Market(s)

Mortgage Professionals

Industry/Entity Type

Mortgage Lender

Font styles to use
Serif
Sans Serif

Colors
9bcb3c
cadf82

Requirements
Must have
• Logo, the words on the image

```html
<!DOCTYPE html>
<html lang="en">
<head>
<meta charset="utf-8">
<title>Brightway Home Loans – Tradeshow Booth</title>
<link href="https://fonts.googleapis.com/css2?family=Roboto+Condensed:wght@700&display=swap" rel="stylesheet">
<style>
  :root {
    --backdrop: #ffffff;
    --header-grey: #e0e0e0;
    --mint: #94c2a8;
    --forest: #1f4a2b;
  }
  * { margin: 0; padding: 0; box-sizing: border-box; }
  html, body {
    width: 1200px;
    height: 1200px;
    overflow: hidden;
    background: var(--backdrop);
  }
  .canvas {
    width: 1200px;
    height: 1200px;
    display: flex;
    align-items: center;
    justify-content: center;
  }
  .booth-panel {
    width: 1200px;
    height: 862px;
    display: flex;
    flex-direction: column;
    font-family: "Roboto Condensed", "Arial Narrow", sans-serif;
    font-weight: 700;
    color: var(--forest);
  }
  .brand-band {
    height: 249px;
    background: var(--header-grey);
    display: flex;
    align-items: center;
    justify-content: center;
  }
  .brand-name {
    font-size: 72px;
    line-height: 1;
    letter-spacing: 1px;
    text-transform: uppercase;
    white-space: nowrap;
  }
  .message-area {
    flex: 1;
    background: var(--mint);
    display: flex;
    flex-direction: column;
    align-items: center;
    padding-top: 153px;
  }
  .tagline {
    font-size: 56px;
    line-height: 50px;
    text-align: center;
    text-transform: uppercase;
    letter-spacing: 0.5px;
  }
  .tagline-rule {
    width: 737px;
    height: 3px;
    background: var(--forest);
    margin: 22px 0 16px;
  }
  .subline {
    font-size: 56px;
    line-height: 56px;
    text-transform: uppercase;
    letter-spacing: 0.5px;
  }
</style>
</head>
<body>
  <main class="canvas">
    <section class="booth-panel">
      <header class="brand-band">
        <span class="brand-name">Brightway Home Loans</span>
      </header>
      <div class="message-area">
        <h1 class="tagline">Innovative Solutions for<br>Non-Traditional Borrowers</h1>
        <div class="tagline-rule" aria-hidden="true"></div>
        <p class="subline">Flexible Guidelines</p>
      </div>
    </section>
  </main>
</body>
</html>
```